Brom Vela CEO and Partners Business Card

We need a fresh, fun, simple and clean business card design....we would like a template where we can add a name and title (as well as specific email addresses). We are open to different looks (full logo on one side and a small logo on the company info side, or our logo is in the background but faint on one side but full on the other, or something else cool :-) ). Our colors are in our logo: blue, black and white...however we are not opposed to the use of other colors if it works. We build sets, make props and a host of other things for the film and television industry...our card should reflect creativity, style and professionalism.

A white background would be preferred.

I would like to see an option with Facebook and Instagram icons.

Facebook- facebook.com/bromvelaqt
Instagram- brom_vela

Our website is bromvela-example.com.

Brom Vela, Inc.
4168 Tolliver Crescent, Unit 9
Ashgrove Park, Westmara 40219
555.210.4872 | tel
555.210.6391 | fax
www.BromVela-example.com

Sample Name and Title #1:

Curtis Welbore
CEO / Co-Owner
555.210.4872 | tel
555.210.6391 | fax
curtis@bromvela-example.com
www.BromVela-example.com

Target Market(s)

Marketing Professionals, Production Designers, Interior Designers, Film Producers, Directors, Art Directors, Event Directors

Industry/Entity Type

Entertainment Industry

Contact Information for Business Card

Curtis Welbore
CEO / Co-Owner
555.210.4872 | tel
555.210.6391 | fax
curtis@bromvela-example.com
www.BromVela-example.com

Font styles to use
Sans Serif

Colors
33a6d7
ffffff
1b1b1b

Requirements
Must have
• Logo, All Contact Info, White Background. Symmetry.
Nice to have
• Facebook and Instagram icons with addresses
• Facebook- facebook.com/bromvelaqt
• Instagram- brom_vela

```html
<!DOCTYPE html>
<html lang="en">
<head>
<meta charset="utf-8">
<title>Brom Vela CEO and Partners Business Card</title>
<link href="https://fonts.googleapis.com/css2?family=Lato:wght@400;700&display=swap" rel="stylesheet">
<style>
  :root {
    --brand-blue: #33a6d7;
    --brand-white: #ffffff;
    --brand-black: #1b1b1b;
    --stage: #e9e9e9;
    --card-shade: #ececec;
  }
  * { box-sizing: border-box; margin: 0; padding: 0; }
  html, body { width: 1200px; height: 780px; overflow: hidden; }
  body {
    background: var(--stage);
    font-family: "Lato", Arial, sans-serif;
    color: var(--brand-black);
    display: flex;
    align-items: center;
    justify-content: center;
    gap: 40px;
  }
  .card {
    position: relative;
    width: 540px;
    height: 309px;
    border-radius: 14px;
    overflow: hidden;
    background: var(--brand-white);
    box-shadow: 0 6px 18px rgba(0,0,0,.14);
  }
  .card-back {
    background: radial-gradient(ellipse at 45% 40%, var(--brand-white) 0%, var(--card-shade) 100%);
    display: flex;
    align-items: center;
    justify-content: center;
  }
  .wordmark {
    font-weight: 700;
    color: var(--brand-black);
    letter-spacing: -1px;
    line-height: 1;
    white-space: nowrap;
  }
  .card-front .wordmark {
    position: absolute;
    top: 34px;
    right: 38px;
    font-size: 46px;
  }
  .card-back .wordmark { font-size: 64px; }

  .person {
    position: absolute;
    left: 34px;
    top: 92px;
  }
  .person-name {
    font-weight: 700;
    font-size: 17px;
    letter-spacing: .3px;
    text-transform: uppercase;
  }
  .person-title {
    font-size: 15px;
    color: var(--brand-blue);
    margin-top: 2px;
  }
  .contact-list {
    list-style: none;
    margin-top: 12px;
  }
  .contact-list li {
    display: flex;
    align-items: center;
    gap: 8px;
    font-size: 13px;
    line-height: 19px;
  }
  .contact-icon {
    width: 14px;
    height: 14px;
    border-radius: 3px;
    background: var(--brand-blue);
    flex: none;
  }
  .address {
    position: absolute;
    left: 300px;
    top: 188px;
    font-size: 13px;
    line-height: 19px;
    font-style: normal;
  }
  .edge-band {
    position: absolute;
    left: 0;
    bottom: 0;
    width: 540px;
    height: 74px;
  }
  .band-site {
    position: absolute;
    bottom: 14px;
    left: 0;
    right: 0;
    text-align: center;
    color: var(--brand-white);
    font-size: 12px;
    letter-spacing: .3px;
  }
</style>
</head>
<body>

  <section class="card card-front" aria-label="Business card front">
    <div class="wordmark">Brom Vela</div>

    <div class="person">
      <p class="person-name">Curtis Welbore</p>
      <p class="person-title">CEO / Co-Owner</p>
      <ul class="contact-list">
        <li>
          <svg class="contact-icon" viewBox="0 0 14 14" aria-hidden="true"><rect width="14" height="14" rx="3" fill="#33a6d7"/><path d="M4 3.5c.6-.4 1.2 0 1.5.8l.3.8c.1.4 0 .7-.3 1 .4.9 1 1.5 1.9 1.9.3-.3.6-.4 1-.3l.8.3c.8.3 1.2.9.8 1.5-.5.8-1.4 1.1-2.3.7C5.8 9.5 4.5 8.2 3.8 6.4c-.4-.9-.1-2.2.2-2.9z" fill="#fff"/></svg>
          555.210.4872
        </li>
        <li>
          <svg class="contact-icon" viewBox="0 0 14 14" aria-hidden="true"><rect width="14" height="14" rx="3" fill="#33a6d7"/><rect x="3.5" y="3" width="7" height="8" rx="1" fill="none" stroke="#fff" stroke-width="1.2"/><path d="M5 6h4M5 8h4" stroke="#fff" stroke-width="1"/></svg>
          555.210.6391
        </li>
        <li>
          <svg class="contact-icon" viewBox="0 0 14 14" aria-hidden="true"><rect width="14" height="14" rx="3" fill="#33a6d7"/><rect x="3" y="4" width="8" height="6" fill="none" stroke="#fff" stroke-width="1.1"/><path d="M3 4l4 3.2L11 4" fill="none" stroke="#fff" stroke-width="1.1"/></svg>
          curtis@bromvela-example.com
        </li>
        <li>
          <span class="contact-icon" aria-hidden="true"></span>
          brom_vela
        </li>
        <li>
          <svg class="contact-icon" viewBox="0 0 14 14" aria-hidden="true"><rect width="14" height="14" rx="3" fill="#33a6d7"/><circle cx="7" cy="7" r="3.8" fill="none" stroke="#fff" stroke-width="1"/><path d="M3.2 7h7.6M7 3.2c-1.6 2.2-1.6 5.4 0 7.6M7 3.2c1.6 2.2 1.6 5.4 0 7.6" fill="none" stroke="#fff" stroke-width=".9"/></svg>
          www.BromVela-example.com
        </li>
      </ul>
    </div>

    <address class="address">
      4168 Tolliver Crescent, Unit 9<br>
      Ashgrove Park, Westmara 40219
    </address>

    <svg class="edge-band" viewBox="0 0 540 74" preserveAspectRatio="none" aria-hidden="true">
      <path d="M0 74 C140 22 400 22 540 74 Z" fill="#33a6d7"/>
      <path d="M0 72 C140 20 400 20 540 72" fill="none" stroke="#1b1b1b" stroke-width="4"/>
    </svg>
    <p class="band-site">www.BromVela-example.com</p>
  </section>

  <section class="card card-back" aria-label="Business card back">
    <div class="wordmark">Brom Vela</div>
  </section>

</body>
</html>
```